Brimlock Assurance Branding Revamp

We are a consulting company, looking for a way to display and promote our brand. We have 2 sides to the business- Brimlock (financial) and Assurance (cyber security). The financial side products relate to business necessities: card processing, website design/hosting/maintenance, VoIP phone systems. The cyber security side promotes a bundled package of 4 solutions: network vulnerability scan, dark web scan, anti-ransomeware/malware software, and image-level backups. We want people to understand that partnering with Brimlock Assurance gives them “Elevated Peace of Mind” (tagline). Current badge and logos uploaded.

Target Market(s)

Small businesses

Contact Information for Business Card

Carla Whitfield, Vice President, carla@brimlockassurance.example, 555-384-9106, www.brimlockassurance.example

Requirements
Nice to have
• I do prefer the darker background for front and back

```html
<!DOCTYPE html>
<html lang="en">
<head>
<meta charset="utf-8">
<title>Brimlock Assurance — Business Card</title>
<link rel="stylesheet" href="https://fonts.googleapis.com/css2?family=Montserrat:wght@400;500;600&display=swap">
<style>
  :root {
    --stage: #1d1d1f;
    --card: #141414;
    --red: #e3202a;
    --white: #f2f2f2;
    --muted: #d6d6d6;
  }
  * { box-sizing: border-box; margin: 0; padding: 0; }
  html, body {
    width: 1200px; height: 900px; overflow: hidden;
    background: var(--stage);
    font-family: "Montserrat", sans-serif;
  }
  .stage {
    width: 1200px; height: 900px;
    display: flex; flex-direction: column;
    align-items: center; justify-content: center; gap: 48px;
  }
  .card {
    position: relative;
    width: 640px; height: 366px;
    background: var(--card);
    border-left: 2px solid var(--red);
    border-bottom: 3px solid var(--red);
    overflow: hidden;
  }

  /* Front */
  .brand {
    position: absolute; left: 60px; top: 58px;
    display: flex; align-items: center; gap: 14px;
  }
  .brand-square { width: 16px; height: 16px; background: var(--red); }
  .brand-name {
    color: var(--white); font-weight: 500;
    font-size: 22px; letter-spacing: 0.32em; text-transform: uppercase;
  }
  .person {
    position: absolute; right: 60px; top: 120px; text-align: right;
  }
  .person-name {
    color: var(--red); font-weight: 500; font-size: 30px;
    letter-spacing: 0.04em; text-transform: uppercase; line-height: 1.1;
  }
  .person-role {
    color: var(--white); font-weight: 400; font-size: 15px;
    letter-spacing: 0.08em; text-transform: uppercase; margin-top: 4px;
  }
  .rule {
    position: absolute; left: 60px; right: 60px; top: 198px;
    height: 1px; background: var(--red);
  }
  .edge-tab {
    position: absolute; right: 0; top: 176px;
    width: 12px; height: 46px; background: var(--red);
  }
  .contact {
    position: absolute; left: 60px; top: 236px;
    list-style: none; display: flex; flex-direction: column; gap: 10px;
  }
  .contact li {
    display: flex; align-items: center; gap: 10px;
    color: var(--muted); font-size: 14px; font-weight: 400;
  }
  .contact svg { width: 13px; height: 13px; flex: none; }

  /* Back */
  .back-brand {
    position: absolute; inset: 0;
    display: flex; align-items: center; justify-content: center; gap: 18px;
  }
  .back-brand .brand-square { width: 26px; height: 26px; }
  .back-brand-name {
    color: var(--red); font-weight: 600; font-size: 34px;
    letter-spacing: 0.2em; text-transform: uppercase;
  }
</style>
</head>
<body>
<main class="stage">
  <section class="card card-front" aria-label="Business card front">
    <div class="brand">
      <span class="brand-square"></span>
      <span class="brand-name">Brimlock Assurance</span>
    </div>

    <div class="person">
      <p class="person-name">Carla Whitfield</p>
      <p class="person-role">Vice President</p>
    </div>
    <div class="rule"></div>
    <div class="edge-tab"></div>

    <ul class="contact">
      <li>
        <svg viewBox="0 0 16 16" aria-hidden="true"><path d="M4 1.5l2.5 3-1.5 1.7a9 9 0 0 0 4.8 4.8L11.5 9.5l3 2.5-1.6 2.3c-6 .3-11.5-5.2-11.2-11.2z" fill="none" stroke="#e3202a" stroke-width="1.4"/></svg>
        +1 555-384-9106
      </li>
      <li>
        <svg viewBox="0 0 16 16" aria-hidden="true"><rect x="1.5" y="3.5" width="13" height="9" fill="none" stroke="#e3202a" stroke-width="1.4"/><path d="M1.5 3.5L8 9l6.5-5.5" fill="none" stroke="#e3202a" stroke-width="1.4"/></svg>
        carla@brimlockassurance.example
      </li>
      <li>
        <svg viewBox="0 0 16 16" aria-hidden="true"><circle cx="8" cy="8" r="6.5" fill="none" stroke="#e3202a" stroke-width="1.4"/><path d="M1.5 8h13M8 1.5c-3 3.5-3 9.5 0 13M8 1.5c3 3.5 3 9.5 0 13" fill="none" stroke="#e3202a" stroke-width="1.2"/></svg>
        www.brimlockassurance.example
      </li>
    </ul>
  </section>

  <section class="card card-back" aria-label="Business card back">
    <div class="back-brand">
      <span class="brand-square"></span>
      <span class="back-brand-name">Brimlock</span>
    </div>
  </section>
</main>
</body>
</html>
```